Brightpath Dental Studio

Please go to www.brightpathdentalstudio.example and obtain the current company logo.
Doctors name are
Marita Velbonne, DDS
Denis Kalb, DMD
Addresses are
318 Larchmont Ave
Teaneck, NJ 07666
201-555-0147
And
872 14th St.
West New York, NJ 07093
201-555-0182
Theme of the business card should feel modrrn and similar to the website.
Front side should include company logo, doctors name, addresses, phone numbers.
Back of the card should include blank lines for patient's name. Date and time for next scheduled appointment. And notice of 24-hr cancellation courtesy policy.
Dental

```html
<!DOCTYPE html>
<html lang="en">
<head>
<meta charset="utf-8">
<title>Brightpath Dental Studio — Business Card</title>
<link href="https://fonts.googleapis.com/css2?family=Lato:wght@400;700;900&display=swap" rel="stylesheet">
<style>
  :root {
    --stage: #2e2e2e;
    --card: #f7f7f7;
    --ink: #1e1e1e;
    --ink-soft: #5a5a5a;
    --ink-faint: #b9b9b9;
    --tab: #8c8c8c;
    --rule: #3a3a3a;
    --accent: #2c3a8c;
  }
  * { box-sizing: border-box; margin: 0; padding: 0; }
  html, body {
    width: 1200px; height: 997px; overflow: hidden;
    background: var(--stage);
    font-family: "Lato", sans-serif;
    color: var(--ink);
  }
  .stage {
    width: 1200px; height: 997px;
    display: flex; flex-direction: column; align-items: center; justify-content: center;
    gap: 60px;
  }
  .card {
    position: relative;
    width: 700px; height: 400px;
    background: linear-gradient(180deg, #ffffff 0%, var(--card) 100%);
    border-radius: 4px;
    overflow: hidden;
  }
  .edge-tab {
    position: absolute; width: 16px; height: 140px;
    background: var(--tab); border-radius: 8px;
  }
  .edge-tab--left { left: -8px; bottom: 40px; }
  .edge-tab--right { right: -8px; top: 40px; }

  .brand {
    display: flex; align-items: center; gap: 12px;
    font-weight: 900; font-size: 36px; letter-spacing: 1px;
    color: var(--ink); text-transform: uppercase; white-space: nowrap;
  }
  .brand__dot {
    width: 22px; height: 22px; border-radius: 50%;
    background: var(--accent); flex: none;
  }

  /* Back */
  .card--back .brand { position: absolute; top: 60px; left: 70px; }
  .appointment { position: absolute; left: 70px; top: 170px; width: 560px; }
  .appointment__title {
    font-size: 22px; letter-spacing: 2px; color: var(--ink-soft);
    text-transform: uppercase; margin-bottom: 22px;
  }
  .appointment__field { position: relative; height: 56px; }
  .appointment__label {
    position: absolute; left: 180px; top: 0;
    font-size: 13px; letter-spacing: 2px; color: var(--ink-faint); text-transform: uppercase;
  }
  .appointment__line {
    position: absolute; left: 0; right: 0; bottom: 12px;
    border-bottom: 2px dotted var(--ink-soft);
  }
  .policy {
    position: absolute; left: 70px; right: 70px; bottom: 34px;
    font-size: 12px; letter-spacing: .5px; color: var(--ink-soft);
  }

  /* Front */
  .card--front .brand { position: absolute; top: 52px; left: 0; right: 0; justify-content: center; }
  .doctors {
    position: absolute; left: 60px; top: 175px; width: 250px; text-align: center;
  }
  .doctor { font-weight: 700; font-size: 20px; letter-spacing: 1.5px; text-transform: uppercase; line-height: 1.2; }
  .doctor + .doctor { margin-top: 32px; }
  .divider {
    position: absolute; left: 340px; top: 140px; width: 2px; height: 200px;
    background: linear-gradient(180deg, transparent, var(--rule) 30%, var(--rule) 70%, transparent);
  }
  .offices { position: absolute; left: 375px; top: 160px; width: 300px; }
  .office + .office { margin-top: 30px; }
  .office__name { font-weight: 900; font-size: 15px; text-transform: uppercase; letter-spacing: .5px; }
  .office__address { font-size: 14px; color: var(--ink-soft); margin-top: 3px; }
  .office__phone { display: flex; align-items: center; gap: 8px; font-size: 15px; color: var(--ink-soft); margin-top: 4px; }
</style>
</head>
<body>
<main class="stage">

  <section class="card card--back" aria-label="Card back">
    <span class="edge-tab edge-tab--left"></span>
    <span class="edge-tab edge-tab--right"></span>
    <div class="brand"><span class="brand__dot"></span>Brightpath Dental Studio</div>
    <div class="appointment">
      <p class="appointment__title">Your next appointment with us</p>
      <div class="appointment__field">
        <span class="appointment__label">Patient name</span>
        <span class="appointment__line"></span>
      </div>
      <div class="appointment__field">
        <span class="appointment__label">Date &amp; time</span>
        <span class="appointment__line"></span>
      </div>
    </div>
    <p class="policy">As a courtesy, please give at least 24 hours’ notice to cancel or reschedule.</p>
  </section>

  <section class="card card--front" aria-label="Card front">
    <span class="edge-tab edge-tab--left"></span>
    <span class="edge-tab edge-tab--right"></span>
    <div class="brand"><span class="brand__dot"></span>Brightpath Dental Studio</div>

    <div class="doctors">
      <p class="doctor">Marita Velbonne<br>DDS</p>
      <p class="doctor">Denis Kalb<br>DMD</p>
    </div>

    <span class="divider"></span>

    <div class="offices">
      <div class="office">
        <p class="office__name">Teaneck, NJ Office</p>
        <p class="office__address">318 Larchmont Ave Teaneck, NJ 07666</p>
        <p class="office__phone">
          <svg width="16" height="16" viewBox="0 0 16 16" aria-hidden="true"><circle cx="8" cy="8" r="8" fill="#1e1e1e"/><path d="M4 7c0-1.5 1.8-2.6 4-2.6S12 5.5 12 7l-1.5.4-.5-1.2H6l-.5 1.2zM5.5 8h5l.7 3.5h-6.4z" fill="#fff"/></svg>
          201-555-0147
        </p>
      </div>
      <div class="office">
        <p class="office__name">West New York, NJ Office</p>
        <p class="office__address">872 14th St. West New York, NJ 07093</p>
        <p class="office__phone">
          <svg width="16" height="16" viewBox="0 0 16 16" aria-hidden="true"><circle cx="8" cy="8" r="8" fill="#1e1e1e"/><path d="M4 7c0-1.5 1.8-2.6 4-2.6S12 5.5 12 7l-1.5.4-.5-1.2H6l-.5 1.2zM5.5 8h5l.7 3.5h-6.4z" fill="#fff"/></svg>
          201-555-0182
        </p>
      </div>
    </div>
  </section>

</main>
</body>
</html>
```